Vietnamese Restaurant Menu

We are an authentic Vietnamese noodle bar.

We would like our menu redesigned to become more attractive and have a picture for each item. We would like out new menu to look similar to the menu shown on the following website http://quanbepmoc.com.vn/?lang=en

Please find pictures and current menu attached.

If there are any items that you cannot find the pictures for please leave a space and we will add a picture into that slot.

Industry/Entity Type

Restaurant

```html
<!DOCTYPE html>
<html lang="en">
<head>
<meta charset="utf-8">
<title>Lantern Premium Vietnamese Noodle Bar – Menu Spread</title>
<link href="https://fonts.googleapis.com/css2?family=Lato:wght@300;400;700&display=swap" rel="stylesheet">
<style>
  :root {
    --paper: #ffffff;
    --bronze: #9b7b55;
    --ink: #1f1f1f;
    --sketch-paper: #f3f1ed;
    --sketch-mid: #c9c4bc;
    --sketch-dark: #6f6b66;
  }
  * { margin: 0; padding: 0; box-sizing: border-box; }
  html, body { width: 1200px; height: 848px; overflow: hidden; background: var(--paper); }
  .spread {
    position: relative;
    width: 1200px;
    height: 848px;
    background: var(--paper);
    font-family: 'Lato', Arial, sans-serif;
    color: var(--ink);
  }

  .brand-name {
    position: absolute;
    color: var(--bronze);
    font-family: 'Lato', Arial, sans-serif;
    font-weight: 400;
    line-height: 1;
    white-space: nowrap;
  }
  .brand-tagline {
    position: absolute;
    white-space: nowrap;
    font-family: 'Lato', Arial, sans-serif;
  }

  .cover-name { left: 186px; top: 344px; font-size: 108px; }
  .cover-tagline {
    left: 60px; top: 449px;
    font-size: 13.5px; font-weight: 700;
    letter-spacing: 0.1em; color: var(--ink);
  }

  .intro-name { left: 0; right: 0; margin-left: 700px; width: 400px; text-align: center; top: 72px; font-size: 100px; }
  .intro-tagline {
    left: 757px; top: 177px; width: 286px; text-align: center;
    font-size: 15px; font-weight: 400; color: var(--bronze);
  }

  .story {
    position: absolute;
    left: 630px;
    top: 315px;
    width: 538px;
    font-size: 13.9px;
    font-weight: 300;
    line-height: 15.6px;
    text-align: justify;
    hyphens: auto;
    color: #222;
  }
  .story p + p { margin-top: 15.6px; }

  .street-scene {
    position: absolute;
    left: 602px;
    top: 564px;
    width: 598px;
    height: 284px;
    background:
      linear-gradient(90deg, rgba(80,76,70,0.55) 0%, rgba(80,76,70,0) 9%, rgba(80,76,70,0) 88%, rgba(80,76,70,0.5) 100%),
      radial-gradient(ellipse 60% 70% at 55% 70%, rgba(110,104,96,0.45) 0%, rgba(110,104,96,0) 70%),
      linear-gradient(180deg, var(--sketch-paper) 0%, var(--sketch-mid) 55%, var(--sketch-dark) 100%);
  }
</style>
</head>
<body>
<main class="spread">

  <span class="brand-name cover-name">Lantern</span>
  <span class="brand-tagline cover-tagline">PREMIUM VIETNAMESE NOODLE BAR</span>

  <span class="brand-name intro-name">Lantern</span>
  <span class="brand-tagline intro-tagline">PREMIUM VIETNAMESE NOODLE BAR</span>

  <section class="story">
    <p>Lantern Premium Vietnamese Noodle Bar is a modern restaurant concept focused on authentic Vietnamese foods that are served in deep and flavourful broths. Created by a Sydney-based pharmacist, Mai, Lantern Premium Vietnamese Noodle Bar takes your tastebuds on a journey to Vietnam and back. Mai's food is an experience that your tastebuds would not want to miss.</p>
    <p>While working in community pharmacy Mai would daydream about her culinary creations for hours on end. Always on her mind were her favourite Vietnamese noodle dishes originally served in nutritious, deep-flavoured, herb infused broths. She then combined her scientific prowess with her fine tuned tastebuds and experimented day and night for months on end. The results were flavourful recipes that embraced the efforts of and honoured the Vietnamese ancestors that have created such wonderful dishes.</p>
    <p>To fulfil her dreams she would love to share her culinary delights with everyone in Australia and beyond. Most importantly, starting with YOU!</p>
  </section>

  <div class="street-scene" role="img" aria-label="Ink sketch of a busy Vietnamese street with shophouses, trees, overhead wires and street lamps"></div>

</main>
</body>
</html>
```